Vex9Tax Business Card

Need a new business card for my law firm. The major components for the card will be my logo "Vex9Tax," the photo of me, contact information, and a QR Code for my website vex9tax.com. If you are unable to generate a QR Code, let me know and I'll see if I can make one. For the "Vex9Tax" logo, don't worry about the "Ride The Wave" part, you can leave that out. Here are my and the firm details:
Benedicto R Salazar III
Attorney at Law
Address: 250 Harbor Plaza, Suite 400
Dallas, TX 75201
Office #: 877-482-6173
Cell #: 214-657-3381
Fax #: 469-738-5126
Email: vex@vex9tax.com
Website: vex9tax.com

```html
<!DOCTYPE html>
<html lang="en">
<head>
<meta charset="utf-8">
<title>Vex9Tax Business Card</title>
<link rel="stylesheet" href="https://fonts.googleapis.com/css2?family=Montserrat:wght@400;500;600;800&display=swap">
<style>
  :root {
    --backdrop: #8f9093;
    --card: #050505;
    --accent: #17bdea;
    --ink: #ffffff;
    --photo-dark: #0b0b0d;
    --photo-mid: #1d1e26;
  }
  * { box-sizing: border-box; margin: 0; padding: 0; }
  html, body { width: 1200px; height: 876px; overflow: hidden; }
  body {
    background: var(--backdrop);
    font-family: "Montserrat", Arial, sans-serif;
    color: var(--ink);
    position: relative;
  }
  .card {
    position: absolute;
    background: var(--card);
    box-shadow: 0 6px 18px rgba(0,0,0,.35);
    overflow: hidden;
  }

  /* Front (portrait) */
  .card-front { left: 150px; top: 158px; width: 320px; height: 560px; }
  .portrait-photo {
    position: absolute; left: 0; top: 0; width: 100%; height: 306px;
    background: radial-gradient(ellipse at 50% 55%, var(--photo-mid) 0%, var(--photo-dark) 60%, var(--card) 100%);
  }
  .name-band {
    position: absolute; left: 0; top: 310px; width: 100%; height: 66px;
    background: var(--accent);
    padding: 11px 0 0 26px;
  }
  .name-band .person-name { font-weight: 800; font-size: 20px; letter-spacing: .2px; line-height: 1.15; white-space: nowrap; }
  .name-band .person-title { font-weight: 500; font-size: 15px; margin-top: 3px; }

  .contact {
    position: absolute; left: 30px; top: 396px;
    font-size: 13.5px; font-weight: 500; line-height: 20px;
  }
  .contact .address { margin-bottom: 4px; }
  .contact-list { list-style: none; }
  .contact-list li { display: flex; align-items: center; gap: 8px; height: 20px; }
  .contact-list svg { width: 12px; height: 12px; fill: var(--accent); flex: none; }

  /* Back (landscape) */
  .card-back {
    left: 520px; top: 278px; width: 560px; height: 320px;
    display: flex; align-items: center; justify-content: center;
  }
  .brand-name { font-weight: 800; font-size: 64px; letter-spacing: 1px; color: var(--ink); line-height: 1; }
</style>
</head>
<body>
  <section class="card card-front">
    <div class="portrait-photo" role="img" aria-label="Portrait photo of the attorney in a dark suit against a black backdrop"></div>
    <div class="name-band">
      <p class="person-name">Benedicto R Salazar III</p>
      <p class="person-title">Attorney at Law</p>
    </div>
    <div class="contact">
      <p class="address">250 Harbor Plaza, Suite 400<br>Dallas, TX 75201</p>
      <ul class="contact-list">
        <li><svg viewBox="0 0 12 12" aria-hidden="true"><path d="M2.5 1l2 2.2-1 1.3a7 7 0 0 0 4 4l1.3-1 2.2 2-1.3 1.5C5.5 11 1 6.5 1 2.3z"/></svg>877-482-6173</li>
        <li><svg viewBox="0 0 12 12" aria-hidden="true"><path d="M3 0h6v12H3zM4 1.5v7.5h4V1.5z"/></svg>214-657-3381</li>
        <li><svg viewBox="0 0 12 12" aria-hidden="true"><path d="M3 0h5v3H3zM1 4h10v8H1zM3 6v1.5h2V6zm0 2.5V10h2V8.5zm3-2.5v1.5h3V6z"/></svg>469-738-5126</li>
        <li><svg viewBox="0 0 12 12" aria-hidden="true"><path d="M0 2h12v8H0zm1 1v.3l5 3.5 5-3.5V3z"/></svg>vex@vex9tax.com</li>
        <li><svg viewBox="0 0 12 12" aria-hidden="true"><path d="M6 0a6 6 0 1 0 0 12A6 6 0 0 0 6 0zm-1 1.2C4 2.5 3.6 4 3.5 5.5H1.2A4.9 4.9 0 0 1 5 1.2zm2 0a4.9 4.9 0 0 1 3.8 4.3H8.5C8.4 4 8 2.5 7 1.2zM4.6 5.5c.1-1.6.6-3 1.4-4 .8 1 1.3 2.4 1.4 4zm-3.4 1h2.3c.1 1.5.5 3 1.5 4.3A4.9 4.9 0 0 1 1.2 6.5zm3.4 0h2.8c-.1 1.6-.6 3-1.4 4-.8-1-1.3-2.4-1.4-4zm3.9 0h2.3A4.9 4.9 0 0 1 7 10.8c1-1.3 1.4-2.8 1.5-4.3z"/></svg>vex9tax.com</li>
      </ul>
    </div>
  </section>

  <section class="card card-back">
    <h1 class="brand-name">Vex9Tax</h1>
  </section>
</body>
</html>
```